ALL TEXT Social Media Graphics

We are looking for a series of social media graphics for Instagram (new size: 4:5 (1080 x 1350 pixels) ratio that are ALL TEXT. We want the following quotes below on each graphic; one quote per graphic. AND, In very small letters at the bottom of each graphic, add @PaulaWrenLive
The look and feel of these graphics should be complimentary to the color palette attached below; but keep them simple. But the design is up to you; at the end of this document, I provided various samples of all text graphics that I like as examples.
The Quotes are in the attached WORD document
women trying to lose weight

```html
<!DOCTYPE html>
<html lang="en">
<head>
<meta charset="UTF-8">
<title>Summer Reset Quote Graphic</title>
<link href="https://fonts.googleapis.com/css2?family=Antonio:wght@600;700&family=Poppins:wght@600&display=swap" rel="stylesheet">
<style>
  :root {
    --magenta: #ae1558;
    --pink-mid: #e2739f;
    --glow: #fdf2f6;
    --white: #ffffff;
    --ink: #000000;
  }
  html, body {
    margin: 0;
    padding: 0;
    width: 960px;
    height: 1200px;
    overflow: hidden;
    background: var(--magenta);
  }
  .graphic {
    position: relative;
    width: 960px;
    height: 1200px;
    overflow: hidden;
    background:
      radial-gradient(circle 500px at 480px 600px,
        var(--glow) 0%,
        #f4a9c5 35%,
        var(--pink-mid) 62%,
        #c73e78 82%,
        var(--magenta) 100%);
    font-family: "Antonio", "Oswald", sans-serif;
    text-align: center;
  }
  .headline {
    position: absolute;
    top: 86px;
    left: 0;
    right: 0;
    margin: 0;
    font-weight: 700;
    font-size: 91px;
    line-height: 98px;
    letter-spacing: 0;
    text-transform: uppercase;
    color: var(--white);
    text-shadow: 3px 3px 0 var(--ink);
  }
  .tagline {
    position: absolute;
    top: 504px;
    left: 0;
    right: 0;
    margin: 0;
    font-weight: 700;
    font-size: 87px;
    line-height: 91px;
    letter-spacing: -0.5px;
    color: var(--ink);
  }
  .cta-band {
    position: absolute;
    top: 997px;
    left: 0;
    width: 960px;
    height: 77px;
    background: var(--ink);
    display: flex;
    align-items: center;
    justify-content: center;
  }
  .cta-text {
    margin: 0;
    font-weight: 600;
    font-size: 36px;
    text-transform: uppercase;
    color: var(--white);
  }
  .handle {
    position: absolute;
    top: 1112px;
    left: 0;
    right: 0;
    margin: 0;
    font-family: "Poppins", "Helvetica Neue", sans-serif;
    font-weight: 600;
    font-size: 28px;
    color: var(--white);
  }
</style>
</head>
<body>
  <main class="graphic">
    <h1 class="headline">You Can Absolutely<br>Be Down 20–30 Pounds<br>By End of Summer.</h1>
    <p class="tagline">All it Takes is<br>The Right Plan—and<br>You've Found it.</p>
    <div class="cta-band">
      <p class="cta-text">Comment “Sunshine” for the Sunshine Summer Reset!</p>
    </div>
    <p class="handle">@PaulaWrenLive</p>
  </main>
</body>
</html>
```